Poster for a boatshow for Nautical enthusiasts, masculine and high incoming :-)

We need a poster for a boat show. Motorboats and Sailboats is presented in this Boat show (and other nautical topics like diving, wakeboard, kite, surf, fishing, ...)
This boat show is annual and the Poster is for the 2015 edition.

Your concept must be compatible in a landscape format. (We will ourselves adaptations of different formats.)
Width: 210 mm
Height: 297 mm
It's necessary for us to have the source file (vector) for make, later, the different format (flyers, website, ...)

Content of the Poster:
- 1 big picture (from a cheap stock, like Pixorra.com) (NO CLIP ART) on full page or half page. Clip art must be a small detail added on the poster.
- Big title: « Foire fluviale des Brumes » (« des Brumes » must be smaller of « Foire fluviale ».)
- Date: « 13, 14 et 15 novembre 2015 »
- Place: « Vanthier - Genève »
- website: « www.foire-velique.ch » or « foire-velique.ch »
- Please, leave a zone in the poster for sponsors logos
- The « Jet d’eau de Genève » (http://en.wikiverra.org/wiki/Colonne_Bleue) MUST be visible on the poster (in the picture, added like a clip art, or other graphic idea…)

Target Market(s)

Nautical enthusiasts, more masculine, high income.

Industry/Entity Type

Landscape

Font styles to use
Sans Serif

Colors
33a6d7
0892cd
ffffff

Requirements
Must have
• - The style must be modern, dynamic, bright colors, sober-minded.
• - "Jet d’eau de Genève" must be on the poster.
Should not have
• Clipart, cheap designs...
• Design with sea reference (sand, very big boats, ...). The market of the boatshow is around a lake (no sand, no boat more big of 15 meters).

```html
<!DOCTYPE html>
<html lang="fr">
<head>
<meta charset="utf-8">
<title>Foire fluviale des Brumes 2015</title>
<link href="https://fonts.googleapis.com/css2?family=Josefin+Sans:wght@400;600;700&display=swap" rel="stylesheet">
<style>
  :root {
    --page-bg: #ececec;
    --panel-cyan: #3ebfd3;
    --white: #ffffff;
    --sponsor-ink: #3a3f44;
    --cloud-dark: #6f6a62;
    --cloud-light: #efe9dc;
    --haze: #d7dbdd;
    --mountain: #5a7890;
    --shore: #3e5364;
    --lake-bright: #c7cfd4;
    --lake-mid: #8c9ba6;
    --lake-deep: #33495a;
  }
  * { margin: 0; padding: 0; box-sizing: border-box; }
  html, body { width: 971px; height: 1200px; overflow: hidden; }
  body {
    background: var(--page-bg);
    font-family: "Josefin Sans", sans-serif;
    position: relative;
  }
  .poster {
    position: absolute;
    left: 75px;
    top: 20px;
    width: 820px;
    height: 1160px;
    overflow: hidden;
    background: var(--white);
    box-shadow: 0 4px 18px rgba(0,0,0,0.18);
  }
  .hero-photo {
    position: absolute;
    inset: 0;
    background:
      radial-gradient(ellipse 46px 120px at 52% 24%, rgba(255,255,255,0.95) 0%, rgba(255,255,255,0.55) 45%, rgba(255,255,255,0) 100%),
      radial-gradient(ellipse 110px 230px at 16% 71%, rgba(248,248,246,0.85) 0%, rgba(248,248,246,0.35) 50%, rgba(248,248,246,0) 100%),
      radial-gradient(ellipse 520px 140px at 78% 6%, rgba(255,250,238,0.9) 0%, rgba(255,250,238,0) 100%),
      linear-gradient(180deg,
        var(--cloud-dark) 0%,
        #a39c8f 5%,
        var(--cloud-light) 10%,
        var(--haze) 15%,
        var(--mountain) 20%,
        #7f93a3 24%,
        var(--shore) 27%,
        #4a5f70 30%,
        var(--lake-bright) 31%,
        #b5c0c7 40%,
        var(--lake-mid) 58%,
        #5d7282 78%,
        var(--lake-deep) 100%);
  }
  .footer-curve {
    position: absolute;
    left: 0;
    bottom: 0;
    width: 820px;
    height: 95px;
  }
  .title-panel {
    position: absolute;
    left: 170px;
    top: 401px;
    right: 0;
    height: 330px;
    background: var(--panel-cyan);
    color: var(--white);
    padding: 32px 0 0 44px;
    text-transform: uppercase;
  }
  .title-row { display: flex; align-items: center; }
  .title-main {
    font-weight: 700;
    font-size: 96px;
    line-height: 0.88;
    letter-spacing: 1px;
  }
  .title-sub {
    font-weight: 700;
    font-size: 66px;
    line-height: 1;
  }
  .side-block {
    margin-left: 14px;
    font-weight: 400;
    line-height: 1.05;
    text-align: center;
  }
  .venue-name { font-size: 38px; letter-spacing: 1px; }
  .venue-city { font-size: 30px; letter-spacing: 1px; }
  .event-dates { font-size: 30px; letter-spacing: 1px; }
  .event-month { font-size: 26px; }
  .website {
    margin-top: 10px;
    font-size: 34px;
    font-weight: 600;
    letter-spacing: 2px;
  }
  .website .tld { font-size: 22px; text-transform: none; }
  .sponsors {
    position: absolute;
    left: 340px;
    right: 40px;
    bottom: 22px;
    display: flex;
    justify-content: space-between;
    align-items: center;
    color: var(--sponsor-ink);
    font-size: 17px;
    font-weight: 600;
  }
  .sponsor { display: flex; align-items: center; gap: 6px; }
  .sponsor-dot {
    width: 14px; height: 14px; border-radius: 50%;
    background: var(--sponsor-ink);
  }
</style>
</head>
<body>
  <main class="poster">
    <div class="hero-photo" role="img" aria-label="Photo: Geneva harbour under a bright cloudy sky, mountains behind the city shoreline, the tall white Colonne bleue water jet rising at centre, and a racing sailboat heeling across the shimmering lake at lower left"></div>

    <svg class="footer-curve" viewBox="0 0 820 95" preserveAspectRatio="none" aria-hidden="true">
      <path d="M0 95 L0 88 Q420 68 820 0 L820 95 Z" fill="#ffffff"/>
    </svg>

    <section class="title-panel">
      <div class="title-row">
        <span class="title-main">Foire</span>
        <div class="side-block">
          <div class="venue-name">Vanthier</div>
          <div class="venue-city">– Genève –</div>
        </div>
      </div>
      <div class="title-row">
        <span class="title-main">Fluviale</span>
      </div>
      <div class="title-row">
        <span class="title-sub">Des Brumes</span>
        <div class="side-block">
          <div class="event-dates">13–14–15</div>
          <div class="event-month">Nov. 2015</div>
        </div>
      </div>
      <div class="website">Foire-velique<span class="tld">.ch</span></div>
    </section>

    <footer class="sponsors">
      <span class="sponsor">Assurance Lémaris</span>
      <span class="sponsor"><span class="sponsor-dot"></span>Corvane</span>
      <span class="sponsor">Barreurs</span>
    </footer>
  </main>
</body>
</html>
```